Full redesign of dairy products including Yogurts and milk products

We have been selling milk and yogurts over the past 15 years, we are now expanding into a wider range of dairy products to include flavoured milk and a variety of soft cheeses such as cottage cheese etc. It is now the perfect time to redesign our existing product range to give a fresh and new look to our products. Have a look at our website https://rbtolna.co.uk/ for further details. We are rebranding as TORUNDE, I have attached a identify pack to give you a feel of the the design, this is a fresh and bright design that will reflect the fresh and tasteful products we produce. The current milk label cut out is unique to us and I would like to continue using this shape which I have attached, the other labels should be done using regular rectangular rounded edge labels. The following designs are required;
1 x Universal lid (71.5mm) design for all below 120ml Yogurts
-11 x 120 ml Yogurt pot designs
Strawberry
Strawberry Banana
Peach & Apricot
Cherry
Toffee
Vanilla
Natural
Orange
Forest Fruits
Pineapple
Mango
1 x Universal lid (95.5mm)for below yogurts (can be identical to the 120ml Lid)
-4 x 450ml Yogurt Pots
Strawberry
Natural
Toffee
Mango
-1 x Universal (95.5mm) LID for 150ml Greek Yogurt
-4 x Designs for 150ml Greek yogurt POT
Strawberry
Natural
Vanilla
Mango

3 x Flavoured milk labels 2 sizes 250ml & 1lt
Biscotti
Chocolate
Strawberry

Cottage Cheese Lid & Pot 250g

1 x Quark universal Lid (95.5mm)
4 x Quark 250g pots
Natural
Strawberry
Peach & Apricot
Mango

```html
<!DOCTYPE html>
<html lang="en">
<head>
<meta charset="utf-8">
<title>TORUNDE Live Yogurt – Pot Labels and Lids</title>
<link rel="stylesheet" href="https://fonts.googleapis.com/css2?family=Baloo+2:wght@800&family=Marcellus&display=swap">
<style>
  :root{
    --bg:#ececec;
    --white:#f7f5f5;
    --brand-green:#5cb848;
    --ink:#3a3a3a;
    --mango:#e0504a;
    --mango-fruit-a:#f5c21c;
    --mango-fruit-b:#e2473a;
    --forest:#b8337a;
    --forest-fruit-a:#d83a55;
    --forest-fruit-b:#2b2530;
    --pineapple:#f2c215;
    --pineapple-text:#c9a20e;
    --pineapple-fruit-a:#f6d12a;
    --pineapple-fruit-b:#8a7a2e;
  }
  *{box-sizing:border-box;margin:0;padding:0}
  html,body{width:1200px;height:967px;overflow:hidden;background:var(--bg)}
  .range{position:relative;width:1200px;height:967px;display:grid;grid-template-columns:repeat(3,340px);column-gap:50px;justify-content:center;align-content:center;row-gap:36px}
  .flavour--mango{--tone:var(--mango);--title:var(--mango);--fa:var(--mango-fruit-a);--fb:var(--mango-fruit-b)}
  .flavour--forest{--tone:var(--forest);--title:var(--forest);--fa:var(--forest-fruit-a);--fb:var(--forest-fruit-b)}
  .flavour--pineapple{--tone:var(--pineapple);--title:var(--pineapple-text);--fa:var(--pineapple-fruit-a);--fb:var(--pineapple-fruit-b)}

  /* lid */
  .lid{position:relative;width:280px;height:280px;justify-self:center}
  .lid svg{position:absolute;inset:0}
  .lid__ring-text{font:700 7.4px "Baloo 2",sans-serif;letter-spacing:.6px;fill:var(--ink)}
  .lid__brand{position:absolute;top:40px;left:0;right:0;text-align:center;font:800 24px/1 "Baloo 2",sans-serif;color:var(--brand-green);display:flex;gap:6px;justify-content:center;align-items:center}
  .lid__brand::before{content:"";width:10px;height:10px;border-radius:50%;background:var(--brand-green)}
  .lid__title{position:absolute;top:76px;left:0;right:0;text-align:center;font:800 38px/1 "Baloo 2",sans-serif;color:var(--title);letter-spacing:2px}
  .lid__live{position:absolute;top:70px;right:58px;font:800 14px/1 "Baloo 2",sans-serif;color:var(--title)}
  .lid__fruit{position:absolute;top:128px;left:60px;width:160px;height:70px;border-radius:40px;background:linear-gradient(110deg,var(--fa),var(--fb))}

  /* wrap label */
  .label{position:relative;width:340px;height:520px;border-radius:14px;overflow:hidden;background:var(--tone)}
  .label svg{position:absolute;inset:0}
  .label__brand{position:absolute;top:62px;left:0;right:0;display:flex;justify-content:center;align-items:center;gap:10px;font:800 48px/1 "Baloo 2",sans-serif;color:var(--white)}
  .label__brand::before{content:"";width:16px;height:16px;border-radius:50%;background:var(--white)}
  .label__fruit{position:absolute;top:220px;left:60px;width:220px;height:140px;border-radius:70px;background:radial-gradient(circle at 40% 40%,var(--fa),var(--fb))}
  .label__live{position:absolute;top:372px;right:60px;font:800 22px/1 "Baloo 2",sans-serif;color:var(--title)}
  .label__title{position:absolute;top:388px;left:0;right:0;text-align:center;font:800 60px/1 "Baloo 2",sans-serif;color:var(--title);letter-spacing:2px}
  .label__flavour{position:absolute;top:464px;left:0;right:0;text-align:center;font:400 18px/1 "Marcellus",serif;color:var(--ink);letter-spacing:1px}
</style>
</head>
<body>
<main class="range">

  <!-- lids -->
  <section class="lid flavour--mango">
    <svg viewBox="0 0 280 280" aria-hidden="true">
      <defs><path id="ring-mango" d="M140,140 m-122,0 a122,122 0 1,1 244,0 a122,122 0 1,1 -244,0"/></defs>
      <circle cx="140" cy="140" r="138" fill="var(--tone)"/>
      <circle cx="140" cy="140" r="130" fill="var(--white)"/>
      <text class="lid__ring-text"><textPath href="#ring-mango">Fresh live yogurt made with local milk · keep refrigerated below 5°C · enjoy within three days of opening · shake gently before serving ·</textPath></text>
      <circle cx="140" cy="140" r="112" fill="none" stroke="var(--tone)" stroke-width="1" opacity=".35"/>
    </svg>
    <div class="lid__brand">TORUNDE</div>
    <div class="lid__live">LIVE</div>
    <div class="lid__title">YOGURT</div>
    <div class="lid__fruit" role="img" aria-label="Photograph of a cut mango"></div>
  </section>

  <section class="lid flavour--forest">
    <svg viewBox="0 0 280 280" aria-hidden="true">
      <defs><path id="ring-forest" d="M140,140 m-122,0 a122,122 0 1,1 244,0 a122,122 0 1,1 -244,0"/></defs>
      <circle cx="140" cy="140" r="138" fill="var(--tone)"/>
      <circle cx="140" cy="140" r="130" fill="var(--white)"/>
      <text class="lid__ring-text"><textPath href="#ring-forest">Fresh live yogurt made with local milk · keep refrigerated below 5°C · enjoy within three days of opening · shake gently before serving ·</textPath></text>
      <circle cx="140" cy="140" r="112" fill="none" stroke="var(--tone)" stroke-width="1" opacity=".35"/>
    </svg>
    <div class="lid__brand">TORUNDE</div>
    <div class="lid__live">LIVE</div>
    <div class="lid__title">YOGURT</div>
    <div class="lid__fruit" role="img" aria-label="Photograph of raspberries, blackberries and blueberries"></div>
  </section>

  <section class="lid flavour--pineapple">
    <svg viewBox="0 0 280 280" aria-hidden="true">
      <defs><path id="ring-pineapple" d="M140,140 m-122,0 a122,122 0 1,1 244,0 a122,122 0 1,1 -244,0"/></defs>
      <circle cx="140" cy="140" r="138" fill="var(--tone)"/>
      <circle cx="140" cy="140" r="130" fill="var(--white)"/>
      <text class="lid__ring-text"><textPath href="#ring-pineapple">Fresh live yogurt made with local milk · keep refrigerated below 5°C · enjoy within three days of opening · shake gently before serving ·</textPath></text>
      <circle cx="140" cy="140" r="112" fill="none" stroke="var(--tone)" stroke-width="1" opacity=".35"/>
    </svg>
    <div class="lid__brand">TORUNDE</div>
    <div class="lid__live">LIVE</div>
    <div class="lid__title">YOGURT</div>
    <div class="lid__fruit" role="img" aria-label="Photograph of a sliced pineapple"></div>
  </section>

  <!-- pot wrap labels -->
  <section class="label flavour--mango">
    <svg viewBox="0 0 340 520" aria-hidden="true">
      <path d="M0 520 L0 300 C30 200 140 180 210 235 C260 272 305 255 340 190 L340 520 Z" fill="var(--white)"/>
      <path d="M220 250 C270 285 310 265 340 220 L340 240 C305 290 265 300 230 268 Z" fill="var(--white)"/>
    </svg>
    <div class="label__brand">TORUNDE</div>
    <div class="label__fruit" role="img" aria-label="Photograph of a whole and sliced mango"></div>
    <div class="label__live">LIVE</div>
    <div class="label__title">YOGURT</div>
    <div class="label__flavour">MANGO</div>
  </section>

  <section class="label flavour--forest">
    <svg viewBox="0 0 340 520" aria-hidden="true">
      <path d="M0 520 L0 300 C30 200 140 180 210 235 C260 272 305 255 340 190 L340 520 Z" fill="var(--white)"/>
      <path d="M220 250 C270 285 310 265 340 220 L340 240 C305 290 265 300 230 268 Z" fill="var(--white)"/>
    </svg>
    <div class="label__brand">TORUNDE</div>
    <div class="label__fruit" role="img" aria-label="Photograph of raspberries, blackberries and blueberries with a leaf"></div>
    <div class="label__live">LIVE</div>
    <div class="label__title">YOGURT</div>
    <div class="label__flavour">FOREST FRUITS</div>
  </section>

  <section class="label flavour--pineapple">
    <svg viewBox="0 0 340 520" aria-hidden="true">
      <path d="M0 520 L0 300 C30 200 140 180 210 235 C260 272 305 255 340 190 L340 520 Z" fill="var(--white)"/>
      <path d="M220 250 C270 285 310 265 340 220 L340 240 C305 290 265 300 230 268 Z" fill="var(--white)"/>
    </svg>
    <div class="label__brand">TORUNDE</div>
    <div class="label__fruit" role="img" aria-label="Photograph of a pineapple with cut wedges"></div>
    <div class="label__live">LIVE</div>
    <div class="label__title">YOGURT</div>
    <div class="label__flavour">PINEAPPLE</div>
  </section>

</main>
</body>
</html>
```